Marrowby Electric
Business Cards
Marrowby Electric -
Creative Brief
Modern
Peter Marrowby
Owner
17 Orvell St. Brookfield CT. 06804
pete@marrowbyelectric-example.com
www.marrowbyelectric-example.com
E-1 #374620

```html
<!DOCTYPE html>
<html lang="en">
<head>
<meta charset="utf-8">
<title>Marrowby Electric – Stationery</title>
<link href="https://fonts.googleapis.com/css2?family=Montserrat:wght@400;700&display=swap" rel="stylesheet">
<style>
  :root{
    --bg:#e9e6e1;
    --paper:#ffffff;
    --blue:#1f8fc9;
    --blue-dark:#145f8c;
    --navy:#0f2536;
    --ink:#1c1c1c;
    --grey:#7a7a7a;
  }
  *{box-sizing:border-box;margin:0;padding:0}
  html,body{width:1200px;height:336px;overflow:hidden;background:var(--bg);font-family:'Montserrat',sans-serif;color:var(--ink)}
  .canvas{position:relative;width:1200px;height:336px}
  .piece{position:absolute;background:var(--paper);box-shadow:0 2px 6px rgba(0,0,0,.25);overflow:hidden}
  .brand{display:flex;align-items:center;gap:5px;font-weight:700;color:var(--navy);text-transform:uppercase;letter-spacing:.5px;white-space:nowrap}
  .brand .mark{width:9px;height:9px;background:var(--blue);flex:none}
  .brand.small{font-size:6px}
  .brand.small .mark{width:7px;height:7px}
  .brand.light{color:#fff}
  .swoosh{position:absolute;top:0;right:0;height:100%}
  .fineprint{position:absolute;font-size:4px;color:var(--grey);white-space:nowrap}

  .brand-display{position:absolute;left:14px;top:86px;width:116px}
  .brand-display .brand{flex-direction:column;font-size:11px;line-height:1.15;text-align:center;gap:0}
  .brand-display .brand .mark{width:30px;height:30px;margin-bottom:8px}

  .card{left:20px;top:150px;width:120px;height:70px}
  .card .brand{position:absolute;left:8px;top:9px}
  .card .name{position:absolute;left:8px;top:30px;font-size:5.5px;font-weight:700}
  .card .role{position:absolute;left:8px;top:38px;font-size:4.5px;color:var(--grey)}

  .letterhead{top:29px;width:216px;height:290px}
  .letterhead-front{left:168px}
  .letterhead-front .brand{position:absolute;left:16px;top:16px}
  .letterhead-front .fineprint{left:16px;bottom:12px;font-size:3.6px}
  .letterhead-back{left:400px}

  .dl{left:648px;width:216px;height:92px}
  .dl-a{top:100px}
  .dl-b{top:212px}
  .dl .brand{position:absolute;left:12px;top:12px}
  .dl .fineprint{left:12px;top:25px}

  .envelope{left:907px;width:240px}
  .env-back{top:72px;height:76px}
  .env-blue{top:150px;height:76px}
  .env-front{top:228px;height:80px}
  .flap{position:absolute;inset:0;width:100%;height:100%}
  .envelope .brand{position:absolute;left:102px;top:30px}
  .env-back .brand{top:13px}
</style>
</head>
<body>
<main class="canvas">

  <div class="brand-display">
    <div class="brand"><span class="mark"></span>Marrowby<br>Electric</div>
  </div>

  <section class="piece card">
    <div class="brand small"><span class="mark"></span>Marrowby Electric</div>
    <p class="name">Peter Marrowby</p>
    <p class="role">Owner · Lic. No. 000000</p>
    <p class="fineprint" style="left:8px;top:47px">17 Orvell St. Fenwick Hollow 00000</p>
    <p class="fineprint" style="left:8px;top:53px">pete@marrowbyelectric-example.com</p>
    <p class="fineprint" style="left:8px;top:59px">www.marrowbyelectric-example.com</p>
    <svg class="swoosh" viewBox="0 0 26 70" width="26" aria-hidden="true">
      <path d="M26 0 H12 C20 20 6 44 14 70 H26Z" fill="var(--navy)"/>
      <path d="M26 0 H19 C26 22 14 46 20 70 H26Z" fill="var(--blue)"/>
    </svg>
  </section>

  <section class="piece letterhead letterhead-front">
    <div class="brand small"><span class="mark"></span>Marrowby Electric</div>
    <svg class="swoosh" viewBox="0 0 50 290" width="50" aria-hidden="true">
      <path d="M50 0 H26 C44 70 14 140 30 220 C34 248 30 272 24 290 H50Z" fill="var(--navy)"/>
      <path d="M50 0 H38 C52 80 28 150 42 230 C44 252 42 274 40 290 H50Z" fill="var(--blue)"/>
    </svg>
    <p class="fineprint">17 Orvell St. Fenwick Hollow 00000 · pete@marrowbyelectric-example.com</p>
  </section>

  <section class="piece letterhead letterhead-back">
    <svg class="swoosh" viewBox="0 0 80 290" width="80" aria-hidden="true">
      <path d="M80 0 H34 C64 60 20 130 46 200 C58 235 42 268 30 290 H80Z" fill="var(--navy)"/>
      <path d="M80 0 H52 C72 70 38 140 60 210 C68 240 58 270 52 290 H80Z" fill="var(--blue)"/>
    </svg>
  </section>

  <section class="piece dl dl-a">
    <div class="brand small"><span class="mark"></span>Marrowby Electric</div>
    <p class="fineprint">17 Orvell St. Fenwick Hollow 00000</p>
    <svg class="swoosh" viewBox="0 0 24 92" width="24" aria-hidden="true">
      <path d="M24 0 H8 C18 26 2 58 12 92 H24Z" fill="var(--navy)"/>
      <path d="M24 0 H16 C24 28 10 60 18 92 H24Z" fill="var(--blue)"/>
    </svg>
  </section>

  <section class="piece dl dl-b">
    <div class="brand small"><span class="mark"></span>Marrowby Electric</div>
    <p class="fineprint">17 Orvell St. Fenwick Hollow 00000</p>
    <svg class="swoosh" viewBox="0 0 24 92" width="24" aria-hidden="true">
      <path d="M24 0 H8 C18 26 2 58 12 92 H24Z" fill="var(--navy)"/>
      <path d="M24 0 H16 C24 28 10 60 18 92 H24Z" fill="var(--blue)"/>
    </svg>
  </section>

  <section class="piece envelope env-back">
    <svg class="flap" viewBox="0 0 240 76" preserveAspectRatio="none" aria-hidden="true">
      <path d="M0 0 H240 L120 40Z" fill="var(--navy)"/>
      <path d="M0 76 L120 38 L240 76Z" fill="#f1f1f1"/>
    </svg>
    <div class="brand small light"><span class="mark"></span>Marrowby</div>
  </section>

  <section class="piece envelope env-blue">
    <svg class="flap" viewBox="0 0 240 76" preserveAspectRatio="none" aria-hidden="true">
      <defs><linearGradient id="flapBlue" x1="0" y1="0" x2="0" y2="1"><stop offset="0" stop-color="var(--blue-dark)"/><stop offset="1" stop-color="var(--blue)"/></linearGradient></defs>
      <rect width="240" height="76" fill="url(#flapBlue)"/>
      <path d="M0 0 H240 L120 26Z" fill="var(--navy)"/>
    </svg>
    <div class="brand small light"><span class="mark" style="background:#fff"></span>Marrowby</div>
  </section>

  <section class="piece envelope env-front">
    <div class="brand small"><span class="mark"></span>Marrowby Electric</div>
  </section>

</main>
</body>
</html>
```